Bramble Hollow Networks - Electrical

We need flyers for electrical services.
Areas of work include new builds, office fitouts, switchboard upgrades, installation of ceiling fans, powerpoint and downlight upgrades, home theatre and AV systems, all exterior and emergency work. Free quotes
We would like to see designs with the colour Red with a young and modern design. Licence No: 63914K must be included and call Leopold on 0438917062.

Colors
ec1f27

```html
<!DOCTYPE html>
<html lang="en">
<head>
<meta charset="utf-8">
<title>Bramble Hollow Networks – Electrical Services Flyer</title>
<link href="https://fonts.googleapis.com/css2?family=Bebas+Neue&family=Montserrat:wght@500;600;700;800&display=swap" rel="stylesheet">
<style>
  :root{
    --red:#ec1f27;
    --black:#050505;
    --maroon:#4a0b10;
    --ink:#1b1b1b;
    --panel:#f3f3f3;
    --white:#ffffff;
    --page:#ffffff;
    --shadow:#9a9a9a;
  }
  *{box-sizing:border-box;margin:0;padding:0}
  html,body{width:1200px;height:2400px;overflow:hidden;background:var(--page)}
  body{position:relative;font-family:"Montserrat",sans-serif;color:var(--ink)}

  .flyer{
    position:absolute;left:40px;top:422px;
    width:756px;height:1050px;
    background:var(--white);
    transform:scale(1.4815);transform-origin:0 0;
    box-shadow:12px 10px 0 var(--shadow);
    overflow:hidden;
  }

  /* Brand */
  .brand{
    position:absolute;right:57px;top:30px;
    display:flex;align-items:center;gap:10px;
  }
  .brand-dot{width:22px;height:22px;border-radius:50%;background:var(--red)}
  .brand-name{font-weight:700;font-size:27px;color:var(--black);letter-spacing:-.3px;white-space:nowrap}

  /* Hero */
  .hero{position:absolute;left:0;top:97px;width:756px;height:390px;background:var(--black)}
  .hero-art{position:absolute;inset:0}
  .headline{
    position:absolute;left:459px;top:60px;
    font-family:"Bebas Neue",sans-serif;line-height:.98;color:var(--white);
  }
  .headline .lead{font-size:46px}
  .headline .accent{font-size:70px;color:var(--red);display:block}
  .headline .accent.big{font-size:80px}
  .headline .tail{font-size:70px;display:block}

  /* Red band with octagon photos */
  .band{position:absolute;left:0;top:487px;width:756px;height:100px;background:var(--red)}
  .octagon{
    position:absolute;top:490px;width:184px;height:184px;
    background:var(--maroon);
    clip-path:polygon(29% 0,71% 0,100% 29%,100% 71%,71% 100%,29% 100%,0 71%,0 29%);
  }
  .octagon .photo{
    position:absolute;inset:6px;
    clip-path:polygon(29% 0,71% 0,100% 29%,100% 71%,71% 100%,29% 100%,0 71%,0 29%);
  }
  .oct-fan{left:55px}
  .oct-fan .photo{background:linear-gradient(160deg,#e9e7e2 0%,#cbbfae 45%,#8a6b55 100%)}
  .oct-av{left:289px}
  .oct-av .photo{background:linear-gradient(110deg,#1f1f22 0%,#3b3d44 40%,#e7ebef 60%,#3c5fa8 100%)}
  .oct-tools{left:523px}
  .oct-tools .photo{background:radial-gradient(circle at 55% 60%,#d7b08e 0%,#a87652 45%,#5b3a2b 100%)}

  /* Services */
  .services-tab{
    position:absolute;left:282px;top:698px;width:192px;height:38px;
    background:var(--red);color:var(--white);
    font-weight:700;font-size:17px;letter-spacing:.6px;
    display:flex;align-items:center;justify-content:center;z-index:2;
  }
  .services{
    position:absolute;left:37px;top:720px;width:678px;height:228px;
    background:var(--panel);
    box-shadow:3px 4px 6px rgba(0,0,0,.18);
  }
  .service-list{position:absolute;list-style:none}
  .service-list.left{left:18px;top:36px}
  .service-list.right{left:395px;top:24px}
  .service{display:flex;align-items:center;gap:14px;font-weight:600;font-size:16.5px;line-height:1.2;color:var(--ink)}
  .service-list.left .service{height:24px;margin-bottom:18px}
  .service-list.left .service:nth-child(3){margin-bottom:19px}
  .service-list.right .service{height:44px;margin-bottom:14px}
  .icon{width:34px;height:34px;flex:none}
  .icon circle.ring{fill:var(--white);stroke:#8a8a8a;stroke-width:1.2}
  .icon .glyph{fill:none;stroke:var(--red);stroke-width:1.4;stroke-linecap:round;stroke-linejoin:round}

  /* Footer */
  .footer{position:absolute;left:0;top:978px;width:756px;height:72px}
  .footer svg{position:absolute;inset:0}
  .free-quotes{position:absolute;left:49px;top:0;height:72px;display:flex;align-items:center;
    color:var(--white);font-weight:700;font-size:17px;letter-spacing:.4px}
  .contact{position:absolute;left:231px;top:0;height:72px;display:flex;align-items:center;gap:9px;color:var(--white);font-weight:700;white-space:nowrap}
  .contact .call{font-size:17px}
  .contact .phone{font-size:27px;color:#2a0608;font-weight:800;letter-spacing:-.3px}
  .contact .licence{font-size:13px;margin-left:8px}
  .contact .licence-no{font-size:17px;font-weight:600;color:#2a0608;letter-spacing:.4px}
</style>
</head>
<body>
<main class="flyer">

  <header class="brand">
    <span class="brand-dot"></span>
    <span class="brand-name">Bramble Hollow Networks</span>
  </header>

  <section class="hero">
    <svg class="hero-art" viewBox="0 0 756 390" width="756" height="390">
      <defs>
        <linearGradient id="electricianTones" x1="0" y1="0" x2="1" y2="1">
          <stop offset="0" stop-color="#3a4a5c"/>
          <stop offset=".45" stop-color="#b9746f"/>
          <stop offset=".75" stop-color="#c99a55"/>
          <stop offset="1" stop-color="#2c3440"/>
        </linearGradient>
        <linearGradient id="chevronRed" x1="0" y1="0" x2="1" y2="0">
          <stop offset="0" stop-color="#7d0a10"/>
          <stop offset="1" stop-color="#ec1f27"/>
        </linearGradient>
      </defs>
      <polygon role="img" aria-label="Photo of a female electrician in a hard hat and safety glasses working overhead"
        points="0,0 300,0 392,195 300,390 0,390" fill="url(#electricianTones)"/>
      <polygon points="318,40 350,40 430,210 350,390 318,390 398,210" fill="url(#chevronRed)"/>
      <polygon points="0,80 30,80 110,210 30,340 0,340 80,210" fill="url(#chevronRed)"/>
    </svg>
    <h1 class="headline">
      <span class="lead">We provide best</span>
      <span class="accent">Electrical</span>
      <span class="accent big">Services</span>
      <span class="tail">In this city</span>
    </h1>
  </section>

  <div class="band"></div>
  <div class="octagon oct-fan"><div class="photo" role="img" aria-label="Photo of an electrician installing a ceiling fan light"></div></div>
  <div class="octagon oct-av"><div class="photo" role="img" aria-label="Photo of a technician setting up home theatre speakers"></div></div>
  <div class="octagon oct-tools"><div class="photo" role="img" aria-label="Photo of an electrician in a hard hat working with gloved hands"></div></div>

  <h2 class="services-tab">OUR SERVICES</h2>
  <section class="services">
    <ul class="service-list left">
      <li class="service">
        <svg class="icon" viewBox="0 0 34 34"><circle class="ring" cx="17" cy="17" r="16"/><path class="glyph" d="M9 24h16M11 24v-8l6-5 6 5v8M15 24v-5h4v5"/></svg>
        New builds</li>
      <li class="service">
        <svg class="icon" viewBox="0 0 34 34"><circle class="ring" cx="17" cy="17" r="16"/><path class="glyph" d="M10 25V11h9v14M13 14h3M13 18h3M13 22h3M21 25v-7h4v7"/></svg>
        Office fitouts</li>
      <li class="service">
        <svg class="icon" viewBox="0 0 34 34"><circle class="ring" cx="17" cy="17" r="16"/><path class="glyph" d="M8 12h18v11H8zM11 16h5M11 20h5M19 16h4v4h-4z"/></svg>
        Switchboard upgrades</li>
      <li class="service">
        <svg class="icon" viewBox="0 0 34 34"><circle class="ring" cx="17" cy="17" r="16"/><path class="glyph" d="M17 9v6M8 18l9-2 9 2M17 16v4M15 20h4"/></svg>
        Installation of ceiling fans</li>
    </ul>
    <ul class="service-list right">
      <li class="service">
        <svg class="icon" viewBox="0 0 34 34"><circle class="ring" cx="17" cy="17" r="16"/><path class="glyph" d="M8 17h4M22 17h4M14 12v10M17 10v14M20 12v10"/></svg>
        <span>Powerpoint and<br>downlight upgrades</span></li>
      <li class="service">
        <svg class="icon" viewBox="0 0 34 34"><circle class="ring" cx="17" cy="17" r="16"/><path class="glyph" d="M10 11h14v9H10zM13 24h8M17 20v4"/></svg>
        <span>Home theatre and<br>AV systems</span></li>
      <li class="service">
        <svg class="icon" viewBox="0 0 34 34"><circle class="ring" cx="17" cy="17" r="16"/><path class="glyph" d="M18 8l-6 10h5l-2 8 7-11h-5z"/></svg>
        <span>All exterior and<br>emergency work.</span></li>
    </ul>
  </section>

  <footer class="footer">
    <svg viewBox="0 0 756 72" width="756" height="72">
      <polygon points="0,0 188,0 208,36 188,72 0,72" fill="var(--black)"/>
      <polygon points="200,0 756,0 756,72 200,72 220,36" fill="var(--red)"/>
    </svg>
    <div class="free-quotes">FREE QUOTES</div>
    <div class="contact">
      <span class="call">Call Leopold</span>
      <span class="phone">0438917062</span>
      <span class="licence">Licence No:</span>
      <span class="licence-no">63914K</span>
    </div>
  </footer>

</main>
</body>
</html>
```